Brisklane Provisions' Ferrotide Bulk Builder 7200

Brisklane Provisions supplies Health supplements and have been trading since 1975, mainly to Bodybuilders and weightlifters. Over the years our customers have aged and our range extended to compliment their needs, i.e; more general supplements. However this label is for our Ferrotide Bulk Builder 7200. If you look online you will see this product is in a 3ltr white pot the label currently, is a dark brown background label with red and white lettering, red denoted the flavour of strawberry.
We would like the design to look good and more up to date for both men and women. A white background, with no horizontal lines top and bottom.

```html
<!DOCTYPE html>
<html lang="en">
<head>
<meta charset="utf-8">
<title>Brisklane Provisions – Ferrotide Bulk Builder 7200 label</title>
<link rel="stylesheet" href="https://fonts.googleapis.com/css2?family=Montserrat:ital,wght@0,500;0,700;1,300;1,800;1,900&display=swap">
<style>
  :root {
    --page: #ffffff;
    --label-white: #ffffff;
    --panel-grey: #ececec;
    --ink: #2b2b2d;
    --ink-soft: #4a4a4c;
    --red: #d7141c;
    --red-deep: #a3151b;
    --brown: #7a4a33;
  }
  html, body {
    margin: 0;
    padding: 0;
    width: 1168px;
    height: 1200px;
    overflow: hidden;
    background: var(--page);
  }
  .label {
    display: block;
    width: 1168px;
    height: 1200px;
    font-family: "Montserrat", sans-serif;
  }
  .brand-strip { fill: var(--label-white); }
  .texture-panel { fill: var(--panel-grey); }
  .brand-name { fill: var(--ink); font-weight: 500; }
  .product-line-1 { fill: var(--ink); font-style: italic; font-weight: 300; font-size: 70px; }
  .product-line-2 { fill: var(--ink); font-style: italic; font-weight: 900; font-size: 90px; }
  .product-number { fill: var(--red); font-style: italic; font-weight: 900; font-size: 80px; }
  .corner-flag { fill: url(#flagShade); }
  .claim-band { fill: var(--red); }
  .claim-text { fill: #ffffff; font-weight: 500; font-size: 29px; }
  .speed-slash { stroke-width: 5; }
  .benefit { fill: var(--ink-soft); font-weight: 700; font-size: 26px; letter-spacing: 2px; }
  .flavour { fill: var(--red); font-style: italic; font-weight: 800; font-size: 26px; letter-spacing: 1px; }
  .net-weight { fill: var(--ink); font-style: italic; font-weight: 900; font-size: 46px; }
</style>
</head>
<body>
<svg class="label" viewBox="0 0 1168 1200" xmlns="http://www.w3.org/2000/svg">
  <defs>
    <linearGradient id="flagShade" x1="0" y1="0" x2="1" y2="0">
      <stop offset="0" stop-color="#e0161e"/>
      <stop offset="1" stop-color="#a3151b"/>
    </linearGradient>
  </defs>

  <!-- brand strip -->
  <rect class="brand-strip" x="44" y="140" width="267" height="920"/>
  <g class="brand-name">
    <text transform="translate(202 989) rotate(-90)" font-size="118" textLength="780" lengthAdjust="spacingAndGlyphs">BRISKLANE</text>
    <text transform="translate(262 736) rotate(-90)" font-size="60" textLength="530" lengthAdjust="spacingAndGlyphs">PROVISIONS</text>
  </g>

  <!-- textured product panel -->
  <rect class="texture-panel" x="311" y="140" width="813" height="920" role="img" aria-label="Fine light grey diamond mesh texture"/>

  <!-- corner flag -->
  <polygon class="corner-flag" points="934,202 1085,202 1085,332 934,243"/>

  <!-- product name -->
  <text class="product-line-1" x="330" y="318" textLength="430" lengthAdjust="spacingAndGlyphs">FERROTIDE</text>
  <text class="product-line-2" x="330" y="436" textLength="300" lengthAdjust="spacingAndGlyphs">BULK</text>
  <text class="product-line-2" x="330" y="558" textLength="456" lengthAdjust="spacingAndGlyphs">BUILDER</text>
  <text class="product-number" x="810" y="558" textLength="250" lengthAdjust="spacingAndGlyphs">7200</text>

  <!-- claim band -->
  <polygon class="claim-band" points="336,606 715,606 703,654 336,654"/>
  <text class="claim-text" x="352" y="641">LEAN MUSCLE MASS</text>
  <g class="speed-slashes">
    <line class="speed-slash" x1="734" y1="654" x2="746" y2="606" stroke="#d7141c"/>
    <line class="speed-slash" x1="756" y1="654" x2="768" y2="606" stroke="#cf1a1e"/>
    <line class="speed-slash" x1="778" y1="654" x2="790" y2="606" stroke="#c52220"/>
    <line class="speed-slash" x1="800" y1="654" x2="812" y2="606" stroke="#b82a24"/>
    <line class="speed-slash" x1="822" y1="654" x2="834" y2="606" stroke="#a93428"/>
    <line class="speed-slash" x1="844" y1="654" x2="856" y2="606" stroke="#993d2c"/>
    <line class="speed-slash" x1="866" y1="654" x2="878" y2="606" stroke="#8a4530" stroke-width="4"/>
    <line class="speed-slash" x1="888" y1="654" x2="900" y2="606" stroke="#7a4a33" stroke-width="4"/>
    <line class="speed-slash" x1="910" y1="654" x2="922" y2="606" stroke="#6b4a3a" stroke-width="3"/>
    <line class="speed-slash" x1="932" y1="654" x2="944" y2="606" stroke="#5a4840" stroke-width="3"/>
    <line class="speed-slash" x1="954" y1="654" x2="966" y2="606" stroke="#4a4444" stroke-width="2.5"/>
    <line class="speed-slash" x1="976" y1="654" x2="988" y2="606" stroke="#3e3e40" stroke-width="2"/>
    <line class="speed-slash" x1="998" y1="654" x2="1010" y2="606" stroke="#353537" stroke-width="2"/>
    <line class="speed-slash" x1="1020" y1="654" x2="1032" y2="606" stroke="#2b2b2d" stroke-width="1.5"/>
  </g>

  <!-- benefits -->
  <text class="benefit" x="346" y="715">POWER</text>
  <text class="benefit" x="346" y="780">STRENGTH</text>
  <text class="benefit" x="346" y="845">ENDURANCE</text>

  <!-- footer -->
  <text class="flavour" x="349" y="1014">STRAWBERRY FLAVOUR</text>
  <text class="net-weight" x="1072" y="1003" text-anchor="end">2000g</text>
</svg>
</body>
</html>
```